Stationery Design Project

We need, stationary designs for a store of children and juvenile furniture.
we have the logo. also need tags for the furniture with enought space to include description and options , maybe a 4" x 6" tag.

Target Market(s)

Parents of childrens and teens

Industry/Entity Type

Store

```html
<!DOCTYPE html>
<html lang="en">
<head>
<meta charset="utf-8">
<title>Nestwell Stationery</title>
<link rel="stylesheet" href="https://fonts.googleapis.com/css2?family=Didact+Gothic&family=Montserrat:wght@400;500;600&display=swap">
<style>
  :root {
    --bg: #e9eaeb;
    --paper: #f7f7f7;
    --teal: #5fadb8;
    --grey: #7a7a7a;
    --ink: #6f6f6f;
  }
  * { margin: 0; padding: 0; box-sizing: border-box; }
  html, body { width: 1200px; height: 859px; overflow: hidden; }
  body {
    background: var(--bg);
    font-family: "Montserrat", sans-serif;
    color: var(--ink);
    position: relative;
  }
  .sheet {
    position: absolute;
    background: var(--paper);
    box-shadow: 0 2px 6px rgba(0,0,0,0.12);
    overflow: hidden;
  }
  .brand {
    display: flex;
    align-items: center;
    gap: 8px;
    font-family: "Didact Gothic", sans-serif;
    color: var(--grey);
    letter-spacing: 0.04em;
    white-space: nowrap;
  }
  .brand-mark { background: var(--teal); flex: none; }

  /* Letterhead */
  .letterhead { left: 60px; top: 50px; width: 300px; height: 424px; }
  .letterhead .brand { position: absolute; top: 34px; left: 0; right: 0; justify-content: center; font-size: 17px; }
  .letterhead .brand-mark { width: 16px; height: 16px; }
  .letterhead .contact { position: absolute; left: 18px; right: 18px; bottom: 30px; font-size: 5.2px; line-height: 1.7; color: var(--grey); text-align: center; }
  .band { position: absolute; bottom: 0; height: 6px; }
  .band-grey { background: var(--grey); }
  .band-teal { background: var(--teal); }

  /* Folder */
  .folder { left: 400px; top: 50px; width: 300px; height: 424px; }
  .folder .brand { position: absolute; top: 64px; left: 0; right: 0; justify-content: center; font-size: 24px; }
  .folder .brand-mark { width: 22px; height: 22px; }
  .folder .divider-grey { position: absolute; top: 150px; left: 0; width: 45%; height: 8px; background: var(--grey); }
  .folder .divider-teal { position: absolute; top: 150px; left: 45%; right: 0; height: 8px; background: var(--teal); }
  .folder .pocket { position: absolute; top: 164px; left: 0; right: 0; bottom: 0; background: var(--teal); }

  /* Business cards */
  .card { width: 350px; height: 200px; left: 760px; }
  .card-front { top: 50px; }
  .card-front .brand { position: absolute; left: 26px; top: 86px; font-size: 17px; }
  .card-front .brand-mark { width: 15px; height: 15px; }
  .card-front .details { position: absolute; left: 200px; top: 52px; font-size: 8px; line-height: 1.75; color: var(--grey); }
  .card-front .person { font-weight: 600; color: var(--ink); font-size: 9px; }
  .card-front .role { margin-bottom: 8px; }
  .card-back { top: 274px; background: var(--grey); }
  .card-back .brand { position: absolute; left: 0; right: 0; top: 88px; justify-content: center; font-size: 19px; color: #fff; }
  .card-back .brand-mark { width: 16px; height: 16px; }

  /* Envelopes */
  .envelope { width: 520px; height: 260px; top: 540px; }
  .envelope-front { left: 60px; }
  .envelope-front .brand { position: absolute; left: 0; right: 0; top: 40px; justify-content: center; font-size: 22px; }
  .envelope-front .brand-mark { width: 18px; height: 18px; }
  .envelope-front .return { position: absolute; left: 20px; bottom: 24px; font-size: 6.5px; color: var(--grey); }
  .envelope-front .band { height: 8px; }
  .envelope-back { left: 620px; }
  .envelope-back .flap { position: absolute; left: 0; top: 0; right: 0; height: 104px; background: var(--grey); }
  .envelope-back .brand { position: absolute; left: 0; right: 0; top: 44px; justify-content: center; font-size: 13px; color: #fff; }
</style>
</head>
<body>

<section class="sheet letterhead" aria-label="Letterhead">
  <div class="brand"><span class="brand-mark"></span>Nestwell</div>
  <p class="contact">Unit 4, Cedar Road, Westbrook NSW 2750 · Tel: +61 2 5550 0142 · Fax: +61 2 5550 0143<br>Email: hello@nestwell.com · www.nestwell.com</p>
  <div class="band band-grey" style="left:0;width:40%"></div>
  <div class="band band-teal" style="left:40%;right:0"></div>
</section>

<section class="sheet folder" aria-label="Presentation folder">
  <div class="brand"><span class="brand-mark"></span>Nestwell</div>
  <div class="divider-grey"></div>
  <div class="divider-teal"></div>
  <div class="pocket"></div>
</section>

<section class="sheet card card-front" aria-label="Business card front">
  <div class="brand"><span class="brand-mark"></span>Nestwell</div>
  <div class="details">
    <div class="person">Ella Morgan</div>
    <div class="role">Store Manager</div>
    <div>Tel: +61 2 5550 0142</div>
    <div>Mob: 0400 555 019</div>
    <div>hello@nestwell.com</div>
    <div>www.nestwell.com</div>
  </div>
</section>

<section class="sheet card card-back" aria-label="Business card back">
  <div class="brand"><span class="brand-mark"></span>Nestwell</div>
</section>

<section class="sheet envelope envelope-front" aria-label="Envelope front">
  <div class="brand"><span class="brand-mark"></span>Nestwell</div>
  <p class="return">Unit 4, Cedar Road, Westbrook NSW 2750</p>
  <div class="band band-grey" style="left:0;width:40%"></div>
  <div class="band band-teal" style="left:40%;right:0"></div>
</section>

<section class="sheet envelope envelope-back" aria-label="Envelope back">
  <div class="flap"></div>
  <div class="brand">Nestwell</div>
</section>

</body>
</html>
```